Modern card design needed for building development company

We are looking for a sharp modern new look for our business cards.
We are a New Zealand based company called TKV Ventures NZ LTD that specialises in subdividing large sections, housing and commercial buildings.
We have attached a photo of the current logo and would like to see it improved somehow as it looks a bit dated.
We are open to any colours.

Target Market(s)

Investors, Property buyers

Industry/Entity Type

Investment

Contact Information for Business Card

TKV VENTURES NZ LTD
www.tkvventuresnz.co.nz

Howard Pennick
Phone +64 21 843 192
Email hdpennick@fernmail.co.nz

Font styles to use
Serif
Sans Serif

Colors
0792cd
33a6d7
85cae6
6b449b
886aae
f04a50
ec1f27
f37122
f68d4d

Requirements
Must have
• Please try and make the logo more modern or if you have a similar one we would like to see it.

```html
<!DOCTYPE html>
<html lang="en">
<head>
<meta charset="utf-8">
<title>TKV Ventures NZ LTD – Business Card</title>
<link rel="stylesheet" href="https://fonts.googleapis.com/css2?family=Open+Sans:wght@400;600;700&display=swap">
<style>
  :root {
    --backdrop: #2b2b2b;
    --card: #121212;
    --card-edge: #1c1c1c;
    --gold: #f2b705;
    --gold-deep: #e59e0a;
    --text-light: #e6e6e6;
    --divider: #3a3a3a;
  }
  * { margin: 0; padding: 0; box-sizing: border-box; }
  html, body {
    width: 1200px;
    height: 900px;
    overflow: hidden;
    background: var(--backdrop);
    font-family: "Open Sans", sans-serif;
  }
  .stage {
    position: relative;
    width: 1200px;
    height: 900px;
    display: flex;
    align-items: center;
    justify-content: center;
    gap: 50px;
  }
  .card {
    position: relative;
    width: 500px;
    height: 290px;
    background: var(--card);
    border: 1px solid var(--card-edge);
    border-radius: 18px;
    box-shadow: 0 10px 30px rgba(0,0,0,.45);
    overflow: hidden;
  }

  /* Contact side */
  .card--contact { display: flex; }
  .card__brand-zone {
    width: 50%;
    display: flex;
    align-items: center;
    justify-content: center;
    gap: 10px;
    border-right: 1px solid var(--divider);
  }
  .brand-mark {
    width: 16px;
    height: 16px;
    background: var(--gold);
  }
  .brand-name {
    font-weight: 700;
    font-size: 17px;
    letter-spacing: .06em;
    color: var(--gold);
  }
  .card__details {
    width: 50%;
    padding: 78px 0 0 24px;
  }
  .person-name {
    font-weight: 700;
    font-size: 18px;
    color: var(--gold);
    margin-bottom: 18px;
  }
  .contact-list { list-style: none; }
  .contact-list li {
    display: flex;
    align-items: center;
    gap: 9px;
    font-size: 12.5px;
    color: var(--text-light);
    margin-bottom: 8px;
  }
  .contact-icon { width: 12px; height: 12px; flex: none; }

  /* Brand side */
  .card--brand {
    display: flex;
    align-items: center;
    justify-content: center;
  }
  .brand-lockup {
    display: flex;
    flex-direction: column;
    align-items: center;
    gap: 10px;
  }
  .brand-lockup .brand-mark { width: 22px; height: 22px; }
  .brand-lockup .brand-name { font-size: 26px; }
</style>
</head>
<body>
<main class="stage">
  <section class="card card--contact">
    <div class="card__brand-zone">
      <span class="brand-mark"></span>
      <span class="brand-name">TKV VENTURES</span>
    </div>
    <div class="card__details">
      <p class="person-name">Howard Pennick</p>
      <ul class="contact-list">
        <li>
          <svg class="contact-icon" viewBox="0 0 12 12" aria-hidden="true">
            <path d="M2.5 1h2l1 2.5-1.3.9a6 6 0 0 0 3.4 3.4l.9-1.3L11 7.5v2A1.5 1.5 0 0 1 9.5 11 8.5 8.5 0 0 1 1 2.5 1.5 1.5 0 0 1 2.5 1z" fill="var(--gold)"/>
          </svg>
          +64 21 843 192
        </li>
        <li>
          <svg class="contact-icon" viewBox="0 0 12 12" aria-hidden="true">
            <rect x="0.5" y="2" width="11" height="8" rx="1" fill="var(--gold)"/>
            <path d="M1 2.8 6 6.5l5-3.7" fill="none" stroke="var(--card)" stroke-width="1"/>
          </svg>
          hdpennick@fernmail.co.nz
        </li>
        <li>
          <svg class="contact-icon" viewBox="0 0 12 12" aria-hidden="true">
            <circle cx="6" cy="6" r="5.5" fill="var(--gold)"/>
            <path d="M.5 6h11M6 .5c-2.5 3-2.5 8 0 11M6 .5c2.5 3 2.5 8 0 11" fill="none" stroke="var(--card)" stroke-width=".8"/>
          </svg>
          www.tkvventuresnz.co.nz
        </li>
      </ul>
    </div>
  </section>

  <section class="card card--brand">
    <div class="brand-lockup">
      <span class="brand-mark"></span>
      <span class="brand-name">TKV VENTURES NZ LTD</span>
    </div>
  </section>
</main>
</body>
</html>
```